exciting cleaing project

I need a cleaning website built. It has to be built for a woman. the domain name is velmatidies.net.

I need the designer to find the images and code the site. the site needs to be about five pages.

here are some good examples:

https://www.brisktern.com/gainesville/

http://oakhollowtidy.com/

https://pebbleporchgainesville.com/services/

https://www.hubvox.com/housekeepers/gainesville-fl

https://glintrow.com/

Target Market(s)

home cleaning,

Industry/Entity Type

Cleaning Service

Coding

Coded - Design and coding required

Number of Pages Required

4 page

Font styles to use
Script

Colors
33a6d7
85acd3
f04a50
ec1f27

Requirements
Must have
• nice design
Nice to have
• residential
Should not have
• commercial

```html
<!DOCTYPE html>
<html lang="en">
<head>
<meta charset="utf-8">
<title>Velma Tidies – Residential Cleaning</title>
<link href="https://fonts.googleapis.com/css2?family=Norican&family=Lobster+Two:ital,wght@1,700&family=Jost:wght@400;500;600;700&family=Montserrat:wght@600;700&display=swap" rel="stylesheet">
<style>
:root{
  --blue:#33a6d7;
  --blue-deep:#1d7fc0;
  --soft-blue:#85acd3;
  --red:#ec1f27;
  --coral:#f04a50;
  --ink:#2b2b2b;
  --muted:#8a8a8a;
  --line:#e6e6e6;
  --white:#ffffff;
}
*{margin:0;padding:0;box-sizing:border-box}
html,body{width:1200px;height:3868px;overflow:hidden}
body{position:relative;background:var(--white);font-family:"Jost",sans-serif;color:var(--ink)}
.abs{position:absolute}
.script{font-family:"Norican",cursive;font-weight:400}
.accent{color:var(--red)}
.tagline{font-family:"Lobster Two",cursive;font-style:italic;font-weight:700;color:var(--blue)}
.body-copy{font-size:12px;line-height:21px;color:var(--muted)}

/* header */
.topbar{left:0;top:0;width:1200px;height:39px;background:var(--blue)}
.logo-tab{left:0;top:0;width:250px;height:39px;background:var(--white);border-top-right-radius:40px}
.topbar-info{right:93px;top:11px;font-size:11px;color:var(--white);display:flex;gap:24px}
.topbar-info span{display:flex;align-items:center;gap:6px}
.topbar-info i{display:inline-block;width:16px;height:16px;border-radius:50%;background:#1a2d44}
.logo{left:93px;top:46px;font-family:"Norican",cursive;font-size:22px;color:var(--ink)}
.logo-dot{left:150px;top:24px;width:12px;height:12px;border-radius:50%;background:var(--blue)}
.nav{left:551px;top:56px;display:flex;gap:44px;font-size:10px;color:#555;letter-spacing:.3px}
.nav .active{color:var(--red)}
.nav-cta{left:995px;top:48px;width:111px;height:26px;background:var(--red);color:var(--white);font-size:10px;font-weight:600;display:flex;align-items:center;justify-content:center}

/* hero */
.hero{left:0;top:84px;width:1200px;height:516px;background:linear-gradient(90deg,#c9c3c0 0%,#d9d4d3 28%,#eeedee 50%,#f6f6f7 100%)}
.hero-kicker{left:708px;top:240px;font-family:"Lobster Two",cursive;font-style:italic;font-weight:700;font-size:26px;color:var(--ink)}
.hero-title{left:708px;top:268px;font-size:58px;color:var(--ink);white-space:nowrap}
.hero-desc{left:708px;top:352px;width:360px;font-size:13px;line-height:19px;color:#444}
.btn-red{background:var(--red);color:var(--white);font-size:10px;font-weight:600;display:flex;align-items:center;justify-content:center}
.hero-btn{left:708px;top:408px;width:126px;height:30px}

/* about */
.about-label{left:97px;top:711px;font-size:18px;color:#444}
.about-title{left:95px;top:733px;font-size:40px;white-space:nowrap}
.about-copy{left:95px;top:796px;width:420px}
.video{left:600px;top:670px;width:506px;height:295px;background:linear-gradient(135deg,#5c6b6f,#7a8a88 50%,#a7a49a)}
.video-bar{left:615px;top:917px;width:460px;height:32px;background:rgba(20,20,20,.75)}
.video-side{left:1052px;top:708px;width:30px;height:134px;display:flex;flex-direction:column;gap:6px}
.video-side i{width:30px;height:28px;background:rgba(20,20,20,.8)}

/* provide */
.center{left:0;width:1200px;text-align:center}
.section-title{font-size:42px}
.provide-title{top:1022px}
.provide-tag{top:1082px;font-size:18px}
.provide-copy{top:1112px;padding:0 170px}
.feature{top:1184px;width:340px;text-align:center;font-size:13px;letter-spacing:.3px;color:#333}
.feature svg{display:block;margin:0 auto 12px}

/* alternating */
.split-title{font-size:44px;white-space:nowrap}
.split-tag{font-size:17px}

/* band */
.band{left:0;top:2154px;width:1200px;height:315px;background:linear-gradient(90deg,#2f2f34,#4a4443 45%,#6a615d)}
.band-title{top:2240px;font-size:42px;color:var(--white)}
.band-tag{top:2298px;font-size:18px}
.band-head{top:2332px;font-family:"Montserrat",sans-serif;font-weight:700;font-size:34px;letter-spacing:2px;color:var(--white)}

/* services */
.services-title{top:2525px}
.svc{width:337px;text-align:center;font-family:"Lobster Two",cursive;font-style:italic;font-weight:700;font-size:15px;color:#333}
.svc-icon{display:block;width:70px;height:70px;margin:17px auto 31px;border-radius:12px;background:var(--blue)}
.rule-h{left:93px;top:2788px;width:1013px;height:1px;background:var(--line)}
.rule-v{width:1px;background:var(--line)}
.dot{width:7px;height:7px;border-radius:50%;background:var(--red)}

/* contact */
.contact{left:0;top:3025px;width:1200px;height:420px;background:linear-gradient(180deg,var(--blue-deep),var(--blue))}
.contact-title{top:3065px;font-size:42px;color:var(--white)}
.field{background:var(--white);font-size:10px;color:#888;padding:9px 12px}
.captcha{left:730px;top:3364px;width:95px;height:29px;background:#2d3440;color:#ddd;font-family:"Norican",cursive;font-size:16px;display:flex;align-items:center;justify-content:center;letter-spacing:3px}
.captcha-input{left:832px;top:3364px;width:153px;height:29px;background:var(--blue-deep);border:1px solid #6fc0e6;font-size:9px;color:#d6ecf8;padding:8px 10px}
.captcha-input i{position:absolute;right:8px;top:6px;width:16px;height:16px;border-radius:50%;background:#1b3f7a}
.submit{left:1003px;top:3364px;width:103px;height:29px;background:#19b4ec;color:var(--white);font-size:11px;font-weight:600;display:flex;align-items:center;justify-content:center}

/* footer */
.foot-h{top:3513px;font-family:"Montserrat",sans-serif;font-weight:600;font-size:18px;letter-spacing:.5px;color:#333}
.foot-list{top:3553px;list-style:none;font-size:11px;color:#555;line-height:25.5px}
.foot-list li::before{content:"+";color:var(--blue);margin-right:5px;font-weight:700}
.foot-text{font-size:11px;color:#555;line-height:17px}
.social{display:flex;gap:3px}
.social i{width:22px;height:22px;display:block}
.copyright-rule{left:93px;top:3754px;width:1013px;height:1px;background:var(--line)}
.copyright{top:3784px;font-size:10px;color:#999;letter-spacing:.3px}
</style>
</head>
<body>

<!-- header -->
<div class="abs topbar"></div>
<div class="abs logo-tab"></div>
<div class="abs topbar-info">
  <span><i></i>Call Us: 352-555-0148</span>
  <span><i></i>Mail: hello@velmatidies.net</span>
</div>
<div class="abs logo-dot"></div>
<div class="abs logo">Velma Tidies</div>
<nav class="abs nav">
  <span class="active">HOME</span><span>ABOUT US</span><span>SERVICES</span><span>FAQ'S</span><span>CONTACT US</span>
</nav>
<div class="abs nav-cta">GET IN TOUCH</div>

<!-- hero -->
<div class="abs hero" role="img" aria-label="Photo of a woman in yellow gloves cleaning a window with a squeegee"></div>
<div class="abs hero-kicker">A wide range of</div>
<div class="abs hero-title script">Cleaning <span class="accent">Service</span></div>
<p class="abs hero-desc">A Wide range of Cleaning Services for catering Both Residential and Condos Business...</p>
<div class="abs btn-red hero-btn">VIEW OUR SERVICES</div>

<!-- about -->
<div class="abs about-label">ABOUT US</div>
<h2 class="abs about-title script">Reliable &amp; <span class="accent">Honest</span></h2>
<p class="abs about-copy body-copy">Our mission at Velma's Tidying is simple: to provide high-quality services for our valued clients. Our team goes above and beyond to cater to each project's specific needs. Through open communication and exceptional service, we hope you'll find what you're looking for with our House Cleaning Service. For more information or general inquiries, get in touch today.</p>
<div class="abs video" role="img" aria-label="Video still of a woman in pink gloves cleaning a window with a spray bottle"></div>
<div class="abs video-side"><i></i><i></i><i></i><i></i></div>
<div class="abs video-bar">
  <svg width="460" height="32" viewBox="0 0 460 32">
    <rect x="8" y="8" width="4" height="16" fill="#fff"/><rect x="16" y="8" width="4" height="16" fill="#fff"/>
    <rect x="65" y="14" width="300" height="4" fill="#555"/><rect x="65" y="14" width="6" height="4" fill="#33a6d7"/>
    <text x="385" y="21" fill="#33a6d7" font-family="Jost" font-size="12" font-weight="700">HD</text>
  </svg>
</div>

<!-- what we provide -->
<h2 class="abs center section-title script provide-title">What We <span class="accent">Provide</span></h2>
<div class="abs center tagline provide-tag">Attention to Detail</div>
<p class="abs center body-copy provide-copy">Since its founding, Velma Tidies has been one of the most trusted names in the industry. Hire us for this service and learn how we cater to the needs of each client, ensuring the results you need and deserve.</p>

<div class="abs feature" style="left:92px">
  <svg width="68" height="68" viewBox="0 0 68 68"><circle cx="34" cy="34" r="34" fill="var(--blue)"/><rect x="20" y="22" width="28" height="24" rx="2" fill="none" stroke="#fff" stroke-width="2"/><line x1="20" y1="29" x2="48" y2="29" stroke="#fff" stroke-width="2"/><g fill="#fff"><circle cx="26" cy="35" r="2"/><circle cx="32" cy="35" r="2"/><circle cx="38" cy="35" r="2"/><circle cx="44" cy="35" r="2"/><circle cx="26" cy="41" r="2"/><circle cx="32" cy="41" r="2"/></g></svg>
  WEEKLY
</div>
<div class="abs feature" style="left:430px">
  <svg width="68" height="68" viewBox="0 0 68 68"><circle cx="34" cy="34" r="34" fill="var(--blue)"/><rect x="20" y="21" width="28" height="27" rx="2" fill="none" stroke="#fff" stroke-width="2"/><line x1="20" y1="28" x2="48" y2="28" stroke="#fff" stroke-width="2"/><text x="34" y="43" text-anchor="middle" fill="#fff" font-family="Jost" font-size="11">31</text></svg>
  BI-WEEKLY
</div>
<div class="abs feature" style="left:767px">
  <svg width="68" height="68" viewBox="0 0 68 68"><circle cx="34" cy="34" r="34" fill="var(--blue)"/><rect x="19" y="21" width="30" height="27" rx="2" fill="none" stroke="#fff" stroke-width="2"/><line x1="19" y1="28" x2="49" y2="28" stroke="#fff" stroke-width="2"/><g fill="#fff"><rect x="24" y="32" width="6" height="5"/><rect x="32" y="32" width="6" height="5"/><rect x="24" y="40" width="6" height="5"/><rect x="32" y="40" width="6" height="5"/></g></svg>
  MONTHLY OR CUSTOM CLEANS AVAILABLE
</div>

<!-- move in -->
<h2 class="abs split-title script" style="left:93px;top:1450px">Move In &amp; Out Cleaning</h2>
<div class="abs tagline split-tag" style="left:94px;top:1502px">Expert Service</div>
<p class="abs body-copy" style="left:93px;top:1540px;width:420px">We have the experience and skills necessary to tackle just about every type of job that comes our way. With Velma Tidies, clients know exactly what to expect - professionalism, efficiency and exceptional results.</p>
<div class="abs" style="left:600px;top:1367px;width:506px;height:323px;background:linear-gradient(135deg,#b9a88f,#e3d8c5 55%,#cdbfa8)" role="img" aria-label="Photo of a housekeeper vacuuming a bedroom floor beside a bed"></div>

<!-- deep cleaning -->
<div class="abs" style="left:93px;top:1761px;width:507px;height:322px;background:linear-gradient(135deg,#8aa0c8,#e9ecef 55%,#f0a25a)" role="img" aria-label="Photo of a woman wiping a window with an orange cloth and glove"></div>
<h2 class="abs split-title script" style="left:683px;top:1843px">Deep Cleaning</h2>
<div class="abs tagline split-tag" style="left:684px;top:1895px">Always Prepared</div>
<p class="abs body-copy" style="left:683px;top:1932px;width:420px">Velma Tidies is committed to getting the job done, especially when it comes to this service. You can count on us to be professional, timely, efficient and make sure you're satisfied every step of the way.</p>

<!-- band -->
<div class="abs band" role="img" aria-label="Dimmed photo of a housekeeper making a bed"></div>
<h2 class="abs center script band-title">Modern Bedroom</h2>
<div class="abs center tagline band-tag">Exceptional Service</div>
<div class="abs center band-head">INTRODUCING VELMA TIDIES</div>

<!-- professional services -->
<h2 class="abs center section-title script services-title">Proffesional <span class="accent">Services</span></h2>
<div class="abs rule-h"></div>
<div class="abs rule-v" style="left:430px;top:2714px;height:160px"></div>
<div class="abs rule-v" style="left:770px;top:2714px;height:160px"></div>
<div class="abs dot" style="left:427px;top:2785px"></div>
<div class="abs dot" style="left:767px;top:2785px"></div>

<div class="abs svc" style="left:93px;top:2614px"><svg class="svc-icon" viewBox="0 0 70 70"><rect width="70" height="70" rx="12" fill="var(--blue)"/><rect x="20" y="34" width="30" height="10" fill="#fff"/><rect x="22" y="28" width="11" height="6" fill="#fff"/><rect x="37" y="28" width="11" height="6" fill="#fff"/></svg>Bedroom Interior</div>
<div class="abs svc" style="left:431px;top:2614px"><svg class="svc-icon" viewBox="0 0 70 70"><rect width="70" height="70" rx="12" fill="var(--blue)"/><path d="M19 36 H51 Q49 48 35 48 Q21 48 19 36Z" fill="#fff"/><rect x="21" y="24" width="3" height="12" fill="#fff"/></svg>Bathrooms</div>
<div class="abs svc" style="left:769px;top:2614px"><svg class="svc-icon" viewBox="0 0 70 70"><rect width="70" height="70" rx="12" fill="var(--blue)"/><rect x="20" y="26" width="30" height="18" fill="none" stroke="#fff" stroke-width="2"/><line x1="20" y1="33" x2="50" y2="33" stroke="#fff" stroke-width="2"/></svg>Kitchen</div>
<div class="abs svc" style="left:93px;top:2818px"><svg class="svc-icon" viewBox="0 0 70 70"><rect width="70" height="70" rx="12" fill="var(--blue)"/><rect x="21" y="33" width="28" height="3" fill="#fff"/><rect x="25" y="36" width="2" height="10" fill="#fff"/><rect x="43" y="36" width="2" height="10" fill="#fff"/><rect x="34" y="22" width="2" height="11" fill="#fff"/></svg>Dining Room</div>
<div class="abs svc" style="left:431px;top:2818px"><svg class="svc-icon" viewBox="0 0 70 70"><rect width="70" height="70" rx="12" fill="var(--blue)"/><rect x="21" y="32" width="28" height="10" rx="2" fill="#fff"/><rect x="25" y="26" width="20" height="6" fill="#fff"/></svg>Living Room</div>
<div class="abs svc" style="left:769px;top:2818px"><svg class="svc-icon" viewBox="0 0 70 70"><rect width="70" height="70" rx="12" fill="var(--blue)"/><rect x="20" y="31" width="30" height="11" fill="none" stroke="#fff" stroke-width="2"/><circle cx="35" cy="25" r="4" fill="#fff"/></svg>Kids Rooms</div>

<!-- contact -->
<div class="abs contact"></div>
<h2 class="abs center script contact-title">Get In Touch With</h2>
<div class="abs field" style="left:93px;top:3157px;width:250px;height:32px">Name:</div>
<div class="abs field" style="left:349px;top:3157px;width:248px;height:32px">Email:</div>
<div class="abs field" style="left:603px;top:3157px;width:247px;height:32px">Phone:</div>
<div class="abs field" style="left:855px;top:3157px;width:251px;height:32px">Subjects:</div>
<div class="abs field" style="left:93px;top:3196px;width:1013px;height:32px">Address:</div>
<div class="abs field" style="left:93px;top:3235px;width:1013px;height:113px">Message:</div>
<div class="abs captcha">C Ov v</div>
<div class="abs captcha-input">Enter Your Captcha<i></i></div>
<div class="abs submit">SUBMIT</div>

<!-- footer -->
<div class="abs foot-h" style="left:93px">SITEMAP</div>
<ul class="abs foot-list" style="left:93px"><li>Home</li><li>About Us</li><li>Services</li><li>FAQ's</li><li>Contact Us</li></ul>
<div class="abs foot-h" style="left:347px">SERVICES</div>
<ul class="abs foot-list" style="left:347px"><li>Bedroom Interior</li><li>Bathrooms</li><li>Kitchen</li><li>Dining room</li><li>Living room</li><li>Kids rooms</li></ul>
<div class="abs foot-h" style="left:607px">CONTACT US</div>
<div class="abs foot-text" style="left:607px;top:3553px;width:180px">
  <div style="display:flex;gap:6px"><span style="color:var(--blue)">●</span><span>15B lorem Ipsum Dolar Site amet, Glassglow 25 USA</span></div>
  <div style="margin-top:12px;display:flex;gap:6px"><span style="color:var(--blue)">✆</span>352-555-0148</div>
  <div style="margin-top:12px;display:flex;gap:6px"><span style="color:var(--blue)">✉</span>hello@velmatidies.net</div>
  <div style="margin-top:14px;font-weight:600;letter-spacing:.5px;color:#333">FOLLOW US</div>
  <div class="social" style="margin-top:6px"><i style="background:#3b5b9a"></i><i style="background:#2fa8e0"></i><i style="background:#d52020"></i><i style="background:#1b76b0"></i></div>
</div>
<div class="abs foot-h" style="left:915px">OPENING HOURS</div>
<div class="abs foot-text" style="left:915px;top:3556px;width:195px">
  <div><span style="color:var(--blue)">+</span> Contact By Text after 9am -10pm<br>&nbsp;&nbsp;&nbsp;Available Cleaning Time</div>
  <div style="margin-top:6px"><span style="color:var(--blue)">+</span> <span style="color:var(--red)">Weekday Hours Posted</span><br>&nbsp;&nbsp;&nbsp;Mon - Fri: 9am - 5pm</div>
  <div class="field" style="margin-top:10px;border:1px solid #ddd;height:27px;padding:7px 10px;font-size:9px">Enter Email:</div>
  <div class="btn-red" style="margin-top:5px;height:25px;font-size:9px">SUBSCRIBE</div>
</div>
<div class="abs copyright-rule"></div>
<div class="abs center copyright">COPYRIGHT © 2019 <span style="color:var(--blue)">VELMA TIDIES</span>. ALL RIGHTS RESERVED.</div>

</body>
</html>
```